VineGlow Artbook for Okanagan Region, British Columbia

Creating an art book: VineGlow, for the Okanagan Wine Region in British Columbia, Canada. Would like smart, modern, clean and linear...cool, sexy urban, not ugly boring suburban... I need a cover that appeals to the wino in all of us! Title: VineGlow -Marla Pettivan
Updates
Thank you all kindly for your efforts. I have added some files so that you can get a sense of my aesthetic...it's never easy trying to figure it out, is it? I will hopefully have dimensions of book soon...cheers, Marla
would anyone please design a giant wine bottle with the wine label that looks like a label but says vineglow...just curious to see if it works as a design or not...thank you.
Target Market(s)
Designing this wine art book of quotes to wineries in Okanagan BC. Buyer is wine lover and tourist ready to spend his vacation bucks on this wonderful book!
Look and feel

```html
<!DOCTYPE html>
<html lang="en">
<head>
<meta charset="utf-8">
<title>VineGlow — Okanagan Wine Region Art Book Cover</title>
<link rel="stylesheet" href="https://fonts.googleapis.com/css2?family=Archivo+Black&family=Archivo:ital,wght@1,400&display=swap">
<style>
  :root {
    --page-bg: #ffffff;
    --cover-bg: #e9e9eb;
    --wine-red: #7d0614;
    --ink: #231f20;
    --caption: #3c3c3c;
  }
  html, body {
    margin: 0;
    padding: 0;
    width: 1200px;
    height: 1200px;
    overflow: hidden;
    background: var(--page-bg);
  }
  .canvas {
    position: relative;
    width: 1200px;
    height: 1200px;
  }
  .book-cover {
    position: absolute;
    left: 300px;
    top: 55px;
    width: 600px;
    height: 1090px;
    background: var(--cover-bg);
  }
  .book-cover svg {
    display: block;
    width: 600px;
    height: 1090px;
  }
  .title-word {
    font-family: "Archivo Black", "Arial Black", sans-serif;
  }
  .title-vine { fill: var(--wine-red); }
  .title-glow { fill: var(--ink); }
  .region-caption {
    font-family: "Archivo", Arial, sans-serif;
    font-style: italic;
    font-size: 14px;
    fill: var(--caption);
  }
</style>
</head>
<body>
<main class="canvas">
  <section class="book-cover" aria-label="VineGlow book cover">
    <svg viewBox="0 0 600 1090" xmlns="http://www.w3.org/2000/svg">
      <title>VineGlow — Okanagan Wine Region</title>

      <text class="title-word title-vine" x="42" y="510" font-size="610"
            textLength="516" lengthAdjust="spacingAndGlyphs">VINE</text>

      <text class="region-caption" text-anchor="end">
        <tspan x="556" y="548">Okanagan</tspan>
        <tspan x="556" y="566">Wine Region</tspan>
      </text>

      <text class="title-word title-glow" x="42" y="1030" font-size="600"
            textLength="516" lengthAdjust="spacingAndGlyphs">GLOW</text>
    </svg>
  </section>
</main>
</body>
</html>
```